Modern corporate energy/fuel business need business card design

Business card required for company founder. Korvan Advanced Power is a Australian based modern energy/fuel provider. We offer specialised solutions to businesses using fossil fuels through renewable energy solutions.

I would like one side with specific information (name, address etc)

The other side to be bold, professional company name & logo. Striking.

Target Market(s)

B2B. Transport, mining, councils, environmentalist,

Industry/Entity Type

Petroleum

Contact Information for Business Card

Name; Oliver Brentham
Position; Director
Email; obrentham@korvanpower.com.au
Address; PO Box 487, Marlowe Creek, NSW, 2990
Website; www.korvanpower.com.au

Colors

Designer to choose colors to be used in the design.

Requirements
Must have
• Clean, easy to read, professional & strong theme
Should not have
• too many colours, busy layout,

```html
<!DOCTYPE html>
<html lang="en">
<head>
<meta charset="utf-8">
<title>Korvan Advanced Power – Business Card</title>
<link rel="stylesheet" href="https://fonts.googleapis.com/css2?family=Montserrat:wght@600;700&family=Questrial&display=swap">
<style>
  :root {
    --navy: #245779;
    --orange: #f1862a;
    --ink: #2b2b2b;
    --paper: #ffffff;
    --backdrop: #e6e7e9;
  }
  * { box-sizing: border-box; margin: 0; padding: 0; }
  html, body { width: 1200px; height: 900px; overflow: hidden; }
  body {
    background: var(--backdrop);
    font-family: "Questrial", "Century Gothic", sans-serif;
    display: flex;
    flex-direction: column;
    align-items: center;
    justify-content: center;
    gap: 40px;
  }
  .card {
    width: 700px;
    height: 400px;
    position: relative;
    box-shadow: 0 6px 18px rgba(0,0,0,0.12);
  }

  /* Front */
  .card-front {
    background: var(--navy);
    display: flex;
    align-items: center;
    justify-content: center;
  }
  .brand {
    display: flex;
    align-items: center;
    gap: 18px;
  }
  .brand-dot {
    border-radius: 50%;
    background: var(--orange);
    flex: none;
  }
  .brand-name {
    font-family: "Montserrat", sans-serif;
    font-weight: 600;
    letter-spacing: 0.04em;
    line-height: 1.15;
    white-space: nowrap;
  }
  .card-front .brand-dot { width: 84px; height: 84px; }
  .card-front .brand-name { color: var(--paper); font-size: 34px; }

  /* Back */
  .card-back { background: var(--paper); }
  .card-back .brand {
    position: absolute;
    left: 48px;
    top: 150px;
    gap: 14px;
  }
  .card-back .brand-dot { width: 58px; height: 58px; }
  .card-back .brand-name { color: var(--navy); font-size: 19px; }
  .divider {
    position: absolute;
    left: 325px;
    top: 100px;
    width: 2px;
    height: 130px;
    background: var(--orange);
  }
  .contact {
    position: absolute;
    left: 356px;
    top: 92px;
  }
  .person-name {
    font-family: "Montserrat", sans-serif;
    font-weight: 700;
    font-size: 24px;
    color: var(--navy);
  }
  .person-role {
    font-size: 19px;
    color: var(--orange);
    margin-top: 2px;
  }
  .contact-list {
    list-style: none;
    margin-top: 18px;
    display: flex;
    flex-direction: column;
    gap: 10px;
  }
  .contact-list li {
    display: flex;
    align-items: center;
    gap: 10px;
    font-size: 17px;
    color: var(--ink);
    white-space: nowrap;
  }
  .contact-icon { width: 16px; height: 16px; flex: none; }
  .address {
    position: absolute;
    right: 48px;
    bottom: 56px;
    font-size: 19px;
    color: var(--ink);
    white-space: nowrap;
  }
</style>
</head>
<body>
  <section class="card card-front">
    <div class="brand">
      <span class="brand-dot"></span>
      <span class="brand-name">Korvan<br>Advanced Power</span>
    </div>
  </section>

  <section class="card card-back">
    <div class="brand">
      <span class="brand-dot"></span>
      <span class="brand-name">Korvan<br>Advanced Power</span>
    </div>
    <div class="divider"></div>
    <div class="contact">
      <p class="person-name">Oliver Brentham</p>
      <p class="person-role">Director</p>
      <ul class="contact-list">
        <li>
          <svg class="contact-icon" viewBox="0 0 16 16" aria-hidden="true">
            <rect x="1" y="3" width="14" height="10" rx="1" fill="#245779"/>
            <path d="M1.5 4 L8 9 L14.5 4" fill="none" stroke="#fff" stroke-width="1.4"/>
          </svg>
          obrentham@korvanpower.com.au
        </li>
        <li>
          <svg class="contact-icon" viewBox="0 0 16 16" aria-hidden="true">
            <circle cx="8" cy="8" r="7" fill="#245779"/>
            <ellipse cx="8" cy="8" rx="3" ry="7" fill="none" stroke="#fff" stroke-width="1"/>
            <line x1="1" y1="8" x2="15" y2="8" stroke="#fff" stroke-width="1"/>
          </svg>
          www.korvanpower.com.au
        </li>
      </ul>
    </div>
    <p class="address">PO Box 487, Marlowe Creek, NSW, 2990</p>
  </section>
</body>
</html>
```